Business card design for industrial spray painting - startup business

Design the layout of our new business card using the logo we have provided.

We want the card to be matt black in colour.

We only want our logo and slogan on the face side.

Because the card is black we would like the slogan WE PAINT ANYTHING! to be in white.

We want our information on the rear side.

I would like my name in blue matching the blue in the logo.

The remainder of the information should be in grey to match the grey in the logo.

The overall finish should look minimal, clean and slick.

Our business is industrlal and of a masculine nature.

Target Market(s)

industrial and mining companies

Contact Information for Business Card

(front of card – matt black)
insert logo here:
insert this tag line: WE PAINT ANYTHING!

--------------------------------------------------------------------------------------------------------------

(back of card – matt black)
Dorian Pelkey
Paint and Coatings Specialist
47 Holloway Crescent, Kenwick WA 6107
M: +61 431 872 914
T: +61 8 555 7136
E: dorian@gleamcoat.co
W: www.gleamcoat.co

Font styles to use
Sans Serif

Colors
000000
0455a3

Requirements
Must have
• clean, slick minimalist look. Masculine as we deal mostly with industrial spray painting

```html
<!DOCTYPE html>
<html lang="en">
<head>
<meta charset="utf-8">
<title>Gleam Coat – Business Card</title>
<link rel="stylesheet" href="https://fonts.googleapis.com/css2?family=Michroma&family=Roboto:wght@400&display=swap">
<style>
  :root {
    --stage: #8c8c8c;
    --card-black: #2a2a2a;
    --brand-blue: #1e76c0;
    --brand-grey: #808184;
    --text-light: #f2f2f2;
    --rule: #bdbdbd;
  }
  html, body {
    margin: 0;
    width: 1200px;
    height: 1200px;
    overflow: hidden;
    background: var(--stage);
  }
  .stage {
    position: relative;
    width: 1200px;
    height: 1200px;
  }
  .card {
    position: absolute;
    top: 310px;
    height: 595px;
    box-shadow: 2px 3px 6px rgba(0,0,0,0.35);
  }
  .card-info {
    left: 234px;
    width: 364px;
    background: var(--card-black);
    color: var(--text-light);
    text-align: center;
    font-family: "Roboto", Arial, sans-serif;
  }
  .wordmark {
    position: absolute;
    top: 165px;
    left: 0;
    right: 0;
    display: flex;
    justify-content: center;
    align-items: center;
    gap: 12px;
    font-family: "Michroma", sans-serif;
    font-size: 22px;
    color: var(--brand-blue);
    letter-spacing: 1px;
  }
  .wordmark .mark-square {
    width: 18px;
    height: 18px;
    background: var(--brand-blue);
  }
  .tagline {
    position: absolute;
    top: 236px;
    left: 0;
    right: 0;
    font-family: "Michroma", sans-serif;
    font-size: 14px;
    letter-spacing: 2px;
    color: #ffffff;
  }
  .person-name {
    position: absolute;
    top: 320px;
    left: 0;
    right: 0;
    font-family: "Michroma", sans-serif;
    font-size: 20px;
    letter-spacing: 1px;
  }
  .person-name .first { color: var(--brand-blue); }
  .person-name .last { color: var(--brand-grey); }
  .role {
    position: absolute;
    top: 351px;
    left: 0;
    right: 0;
    font-size: 17px;
  }
  .contact-divider {
    position: absolute;
    top: 386px;
    left: 85px;
    width: 194px;
    height: 24px;
  }
  .contact-lines {
    position: absolute;
    top: 418px;
    left: 0;
    right: 0;
    font-size: 17px;
    line-height: 21.5px;
  }
  .rule {
    position: absolute;
    top: 493px;
    left: 80px;
    width: 204px;
    height: 1px;
    background: var(--rule);
  }
  .address {
    position: absolute;
    top: 505px;
    left: 0;
    right: 0;
    font-size: 17px;
    line-height: 22px;
  }
  .card-brand {
    left: 627px;
    width: 370px;
    background: var(--brand-grey);
    overflow: hidden;
  }
  .card-brand svg.field {
    position: absolute;
    inset: 0;
  }
  .website {
    position: absolute;
    top: 529px;
    left: 0;
    right: 0;
    text-align: center;
    font-family: "Michroma", sans-serif;
    font-size: 16px;
    letter-spacing: 1px;
    color: #ffffff;
  }
</style>
</head>
<body>
<div class="stage">

  <section class="card card-info">
    <div class="wordmark"><span>GLEAM COAT</span><span class="mark-square"></span></div>
    <div class="tagline">WE PAINT ANYTHING!</div>

    <div class="person-name"><span class="first">DORIAN</span> <span class="last">PELKEY</span></div>
    <div class="role">Paint and Coatings Specialist</div>

    <svg class="contact-divider" viewBox="0 0 194 24" aria-hidden="true">
      <line x1="0" y1="12" x2="58" y2="12" stroke="#bdbdbd" stroke-width="1"/>
      <line x1="136" y1="12" x2="194" y2="12" stroke="#bdbdbd" stroke-width="1"/>
      <circle cx="73" cy="12" r="11" fill="#1e76c0"/>
      <rect x="69" y="5" width="8" height="14" rx="1.5" fill="none" stroke="#2a2a2a" stroke-width="1.6"/>
      <circle cx="97" cy="12" r="11" fill="#1e76c0"/>
      <path d="M90 11 q7 -6 14 0 l-2 2 h-2 v-2 h-6 v2 h-2 z M92 14 h10 v4 h-10 z" fill="#2a2a2a"/>
      <circle cx="121" cy="12" r="11" fill="#1e76c0"/>
      <rect x="115" y="8" width="12" height="8" fill="#2a2a2a"/>
      <path d="M115 8 l6 5 l6 -5" fill="none" stroke="#1e76c0" stroke-width="1"/>
    </svg>

    <div class="contact-lines">
      <div>+61 431 872 914</div>
      <div>+61 8 555 7136</div>
      <div>dorian@gleamcoat.co</div>
    </div>
    <div class="rule"></div>
    <div class="address">
      <div>47 Holloway Crescent</div>
      <div>Kenwick WA 6107</div>
    </div>
  </section>

  <section class="card card-brand">
    <svg class="field" viewBox="0 0 370 595" aria-hidden="true">
      <polygon points="0,0 370,0 370,250 0,420" fill="#1e76c0"/>
    </svg>
    <div class="website">WWW.GLEAMCOAT.CO</div>
  </section>

</div>
</body>
</html>
```